Mara Lindqvist Advisory Business Cards

Hi - using the information and logo provided I require a two sided business card designed with the following information. The business card is a 'mini card' 3.5" x 1.25".

Front of card should be the logo attached but inverted (so the background is the peach colour and the logo white).

Back should have these details. If we can't fit the Instragram and Facebook part can we just put the little logos.

Mara Lindqvist

Art and Design Consultant
Dealer - Curator - Events - Styling - Creative Sourcing

P: 0438 519 207
E: mara@maralindqvistadvisory.com
W: www.maralindqvistadvisory.com
I (instagram image please): maralindqvistadvisory F (Facebook image please): MaraLindqvistAdvisor

Target Market(s)

Galleries, artists, art buyers, interior design clients, event managers, creative types

Industry/Entity Type

Business

```html
<!DOCTYPE html>
<html lang="en">
<head>
<meta charset="utf-8">
<title>Mara Lindqvist Advisory – Mini Business Cards</title>
<link href="https://fonts.googleapis.com/css2?family=Libre+Baskerville&family=Josefin+Slab:wght@600&family=Open+Sans:wght@600&display=swap" rel="stylesheet">
<style>
  :root {
    --peach: #f3b89c;
    --peach-soft: #f7cdb8;
    --peach-pale: #fbe6db;
    --slate: #6a6a6a;
    --ink: #111111;
    --paper: #ffffff;
    --shadow: rgba(0,0,0,0.55);
  }
  * { margin: 0; padding: 0; box-sizing: border-box; }
  html, body { width: 1200px; height: 848px; overflow: hidden; background: var(--paper); }
  .canvas { position: relative; width: 1200px; height: 848px; }

  .card {
    position: absolute; left: 91px; width: 1049px;
    background: var(--paper); overflow: hidden;
    box-shadow: -10px 10px 14px var(--shadow);
  }
  .card--front { top: 18px; height: 377px; }
  .card--back { top: 438px; height: 374px; }

  .band { position: absolute; left: 0; width: 100%; }
  .band--slate { background: var(--slate); }
  .band--peach { background: var(--peach); }

  .wash {
    position: absolute;
    background: radial-gradient(ellipse at 40% 40%, var(--peach-soft) 0%, var(--peach-pale) 55%, rgba(251,230,219,0) 78%);
  }

  .flip { transform: rotate(180deg); transform-origin: center; }

  .front-name {
    position: absolute; left: 4px; top: 45px; width: 420px;
    font-family: "Libre Baskerville", serif; font-size: 34px;
    letter-spacing: 5px; color: var(--slate); white-space: nowrap; line-height: 1;
  }
  .front-tagline {
    position: absolute; left: 74px; top: 10px; width: 300px;
    font-family: "Josefin Slab", serif; font-size: 22px; font-weight: 600;
    letter-spacing: 9px; color: var(--peach); line-height: 1; text-align: center;
  }

  .mark {
    position: absolute; border-radius: 50%; background: var(--peach);
    display: flex; align-items: center; justify-content: center; text-align: center;
    font-family: "Libre Baskerville", serif; color: var(--paper); line-height: 1.3;
  }
  .mark--front { left: 140px; top: 94px; width: 160px; height: 160px; font-size: 15px; padding: 24px; }
  .mark--back { left: 157px; top: 175px; width: 104px; height: 104px; font-size: 10px; padding: 14px; }

  .contact {
    position: absolute; top: 6px; height: 22px; display: flex; align-items: center; gap: 6px;
    font-family: "Open Sans", sans-serif; font-weight: 600; font-size: 16px; color: var(--ink);
  }
  .contact svg { display: block; }
  .contact--phone { left: 28px; }
  .contact--email { left: 272px; }
  .contact--web { left: 718px; }

  .back-name {
    position: absolute; left: 22px; top: 286px;
    font-family: "Libre Baskerville", serif; font-size: 36px; letter-spacing: 4px;
    color: var(--slate); line-height: 1; white-space: nowrap;
  }
  .back-role {
    position: absolute; left: 24px; top: 325px;
    font-family: "Josefin Slab", serif; font-weight: 600; font-size: 15px;
    letter-spacing: 1.6px; color: var(--ink); line-height: 1;
  }
  .back-services {
    position: absolute; left: 24px; top: 350px;
    font-family: "Josefin Slab", serif; font-weight: 600; font-size: 15px;
    letter-spacing: 3.4px; color: var(--peach); line-height: 1; white-space: nowrap;
  }

  .social {
    position: absolute; left: 996px; top: 326px; width: 240px; height: 42px;
    transform-origin: 0 0; transform: rotate(-90deg);
    display: flex; flex-direction: column; justify-content: space-between;
    font-family: "Open Sans", sans-serif; font-size: 14px; color: var(--ink); line-height: 1;
  }
  .social__item { display: flex; align-items: center; gap: 5px; white-space: nowrap; }
  .social__dot { width: 14px; height: 14px; border: 1.5px solid var(--slate); flex: none; }
  .social__dot--solid { background: var(--ink); border-color: var(--ink); }
</style>
</head>
<body>
<main class="canvas">

  <section class="card card--front" aria-label="Card front">
    <div class="band band--slate" style="top:10px;height:25px;"></div>
    <div class="band band--peach" style="top:45px;height:37px;"></div>
    <div class="wash" role="img" aria-label="Soft peach watercolour stain" style="left:370px;top:70px;width:700px;height:330px;"></div>
    <div class="front-tagline flip">ADVISORY</div>
    <div class="front-name flip">MARA LINDQVIST</div>
    <div class="mark mark--front flip">Mara Lindqvist Advisory</div>
  </section>

  <section class="card card--back" aria-label="Card back">
    <div class="band band--slate" style="top:0;height:38px;"></div>
    <div class="band band--peach" style="top:6px;height:22px;"></div>
    <div class="wash" role="img" aria-label="Soft peach watercolour stain" style="left:320px;top:30px;width:740px;height:340px;"></div>

    <div class="contact contact--phone">
      <svg width="22" height="14" viewBox="0 0 22 14" aria-hidden="true"><path d="M1 5c0-3 5-4 10-4s10 1 10 4l-4 1-1-2H6L5 6 1 5z M5 7h12l2 6H3z" fill="#fff"/></svg>
      <span>0438 519 207</span>
    </div>
    <div class="contact contact--email">
      <svg width="30" height="16" viewBox="0 0 30 16" aria-hidden="true"><rect x="1" y="1" width="28" height="14" fill="none" stroke="#fff" stroke-width="1.5"/><path d="M1 1l14 8 14-8" fill="none" stroke="#fff" stroke-width="1.5"/></svg>
      <span>mara@maralindqvistadvisory.com</span>
    </div>
    <div class="contact contact--web">
      <svg width="18" height="18" viewBox="0 0 18 18" aria-hidden="true"><g fill="none" stroke="#fff" stroke-width="1.2"><circle cx="9" cy="9" r="7.5"/><ellipse cx="9" cy="9" rx="3.5" ry="7.5"/><path d="M1.5 9h15M3 5h12M3 13h12"/></g></svg>
      <span>www.maralindqvistadvisory.com</span>
    </div>

    <div class="mark mark--back">Mara Lindqvist Advisory</div>
    <div class="back-name">MARA LINDQVIST</div>

    <div class="band band--peach" style="top:322px;height:22px;"></div>
    <div class="back-role">Art and Design Consultant</div>
    <div class="band band--slate" style="top:349px;height:21px;"></div>
    <div class="back-services">Dealer ~ Curator ~ Events ~ Styling ~ Creative Sourcing</div>

    <div class="social">
      <div class="social__item"><span class="social__dot"></span><span>MaraLindqvistAdvisor</span></div>
      <div class="social__item"><span class="social__dot social__dot--solid"></span><span>maralindqvistadvisory</span></div>
    </div>
  </section>

</main>
</body>
</html>
```